Eye-catching Card for new church

I would like a card the size of a business card ... that can be used to announce the start of our new church. I would like it to have our logo on the card, my name, and the statement "Coming Soon ... 1.10.2016". I also would like to list our website address and Facebook page and my Chirper account.

Target Market(s)

prospective people looking for a church

Industry/Entity Type

Church

Requirements
Must have
• a focus on Coming Soon ... 1.10.2016
• Brightfold Church logo
Should not have
• church buildings or writings on the cross

```html
<!DOCTYPE html>
<html lang="en">
<head>
<meta charset="utf-8">
<title>Brightfold Church – Coming Soon Card</title>
<link rel="stylesheet" href="https://fonts.googleapis.com/css2?family=Questrial&display=swap">
<style>
  :root {
    --backdrop: #5b6169;
    --card: #3d3d3e;
    --ink: #d9d9da;
    --ink-soft: #c6c6c8;
  }
  * { margin: 0; padding: 0; box-sizing: border-box; }
  html, body {
    width: 1200px;
    height: 900px;
    overflow: hidden;
    background: var(--backdrop);
  }
  .card {
    position: absolute;
    left: 100px;
    top: 164px;
    width: 1000px;
    height: 572px;
    background: var(--card);
    border-radius: 6px;
    font-family: "Questrial", "Century Gothic", sans-serif;
    color: var(--ink);
  }
  .social {
    position: absolute;
    left: 48px;
    top: 44px;
    font-size: 24px;
    line-height: 1.35;
    color: var(--ink-soft);
    letter-spacing: 0.3px;
  }
  .brand {
    position: absolute;
    left: 330px;
    top: 160px;
    width: 600px;
    display: flex;
    align-items: center;
    justify-content: center;
    gap: 20px;
  }
  .brand-dot {
    width: 26px;
    height: 26px;
    border-radius: 50%;
    background: var(--ink);
    flex: none;
  }
  .brand-name {
    font-size: 62px;
    color: var(--ink);
    letter-spacing: 1px;
    white-space: nowrap;
  }
  .announcement {
    position: absolute;
    left: 330px;
    top: 300px;
    width: 600px;
    text-align: center;
    font-size: 52px;
    letter-spacing: 1px;
    white-space: nowrap;
  }
  .website {
    position: absolute;
    left: 330px;
    top: 386px;
    width: 600px;
    text-align: center;
    font-size: 30px;
    color: var(--ink-soft);
    letter-spacing: 0.5px;
  }
</style>
</head>
<body>
  <main class="card">
    <div class="social">
      <p class="social-page">Friendly.com/BrightfoldChurchFM.com</p>
      <p class="social-handle">Chirper : @HollisDc</p>
    </div>

    <div class="brand">
      <span class="brand-dot" aria-hidden="true"></span>
      <span class="brand-name">Brightfold Church</span>
    </div>

    <p class="announcement">Coming soon &nbsp;... 1.10.16</p>
    <p class="website">thebrightfoldchurch.com</p>
  </main>
</body>
</html>
```